Thriving Mexican import business needs a new business card

Need a refresher of our current business card. Looking for a lighter background with the logo on one side. We will want this file to be adjustable so we can change names, emails and mobile numbers.
We are open to ideas but maintaining a professional image is critical.
Thankyou,

Target Market(s)

Anyone in food industry

Industry/Entity Type

Wholesale

Contact Information for Business Card

Mark Vellanoweth
Director
Corvan Products & Liquor Pty Ltd
5B Larkfield Ct, Brimsworth VIC 3051
0491325067 (03) 95147286
mark@corvanimports.com.au
corvanimportedgoodsandspirits.com.au

Font styles to use
Serif
Other font styles liked:
• NeoGram Heavy

Requirements
Must have
• Professional yet memorable
Corvan logo
Nice to have
• Chilli or tequila/mexican food pictures
Should not have
• Dark background

```html
<!DOCTYPE html>
<html lang="en">
<head>
<meta charset="utf-8">
<title>Corvan Products &amp; Liquor – Business Card</title>
<link rel="stylesheet" href="https://fonts.googleapis.com/css2?family=Oswald:wght@700&family=Montserrat:wght@400;500;700&display=swap">
<style>
  :root {
    --ink: #0d0d0d;
    --paper: #ffffff;
    --stage: #e8ebec;
    --food-warm: #c9a25a;
    --food-gold: #e0c27a;
    --food-char: #5a3b2a;
    --food-green: #4f7a32;
    --rule: #ffffff;
  }
  * { margin: 0; padding: 0; box-sizing: border-box; }
  html, body { width: 1200px; height: 900px; overflow: hidden; }
  body {
    background: var(--stage);
    font-family: "Montserrat", sans-serif;
    display: flex;
    align-items: center;
    justify-content: center;
    gap: 48px;
  }
  .card {
    width: 525px;
    height: 300px;
    position: relative;
    overflow: hidden;
    box-shadow: 0 2px 10px rgba(0,0,0,0.12);
  }

  /* Front */
  .card--front { background: var(--paper); }
  .brand {
    position: absolute;
    left: 0; right: 0; top: 70px;
    display: flex;
    align-items: center;
    justify-content: center;
    gap: 18px;
  }
  .brand__square {
    width: 46px; height: 46px;
    background: var(--ink);
  }
  .brand__name {
    font-family: "Oswald", sans-serif;
    font-weight: 700;
    font-size: 76px;
    line-height: 1;
    letter-spacing: 1px;
    text-transform: uppercase;
    color: var(--ink);
  }
  .web-band {
    position: absolute;
    left: 0; right: 0; bottom: 0;
    height: 54px;
    background: var(--ink);
    display: flex;
    align-items: center;
    justify-content: center;
  }
  .web-band__url {
    color: var(--paper);
    font-size: 12.5px;
    font-weight: 500;
    letter-spacing: 2.4px;
    text-transform: uppercase;
  }

  /* Back */
  .card--back { background: var(--ink); }
  .food-strip {
    position: absolute;
    left: 0; top: 16px;
    width: 330px; height: 150px;
    background: linear-gradient(100deg, var(--food-gold) 0%, var(--food-warm) 40%, var(--food-char) 72%, var(--food-green) 100%);
  }
  .back-brand {
    position: absolute;
    right: 26px; top: 110px;
    display: flex;
    align-items: center;
    gap: 12px;
  }
  .back-brand__square {
    width: 30px; height: 30px;
    background: var(--paper);
  }
  .back-brand__name {
    font-family: "Oswald", sans-serif;
    font-weight: 700;
    font-size: 52px;
    line-height: 1;
    text-transform: uppercase;
    color: var(--paper);
  }
  .contact {
    position: absolute;
    left: 22px; top: 180px;
    color: var(--paper);
  }
  .contact__marker {
    position: absolute;
    left: -22px; top: 4px;
    width: 14px; height: 24px;
    background: var(--paper);
  }
  .contact__name {
    font-size: 17px;
    font-weight: 700;
    letter-spacing: 1.2px;
    text-transform: uppercase;
    line-height: 1.1;
  }
  .contact__role {
    font-size: 11.5px;
    margin-bottom: 8px;
  }
  .contact__line {
    display: flex;
    align-items: center;
    gap: 7px;
    font-size: 11.5px;
    line-height: 1.55;
  }
  .icon {
    width: 13px; height: 13px;
    flex: none;
  }
  .contact__gap { margin-left: 8px; }
</style>
</head>
<body>

  <section class="card card--front" aria-label="Business card front">
    <div class="brand">
      <span class="brand__square"></span>
      <span class="brand__name">Corvan</span>
    </div>
    <div class="web-band">
      <span class="web-band__url">corvanimportedgoodsandspirits.com.au</span>
    </div>
  </section>

  <section class="card card--back" aria-label="Business card back">
    <div class="food-strip" role="img" aria-label="Photograph of tortilla chips, roasted tomatillos, grilled steak and greens"></div>

    <div class="back-brand">
      <span class="back-brand__square"></span>
      <span class="back-brand__name">Corvan</span>
    </div>

    <div class="contact">
      <span class="contact__marker"></span>
      <p class="contact__name">Mark Vellanoweth</p>
      <p class="contact__role">Director</p>

      <p class="contact__line">
        <svg class="icon" viewBox="0 0 14 14" fill="none" stroke="#fff" stroke-width="1.2"><rect x="0.6" y="0.6" width="12.8" height="12.8"/><path d="M7 11 C4.5 8 4.5 6.5 4.5 5.5 a2.5 2.5 0 0 1 5 0 c0 1-0 2.5-2.5 5.5z"/></svg>
        5B Larkfield Ct, Brimsworth VIC 3051
      </p>
      <p class="contact__line">
        <svg class="icon" viewBox="0 0 14 14" fill="none" stroke="#fff" stroke-width="1.2"><rect x="0.6" y="0.6" width="12.8" height="12.8"/><path d="M4 3.5 l2 0 l0.8 2 l-1.2 0.9 a5 5 0 0 0 2.2 2.2 l0.9-1.2 l2 0.8 l0 2 a1 1 0 0 1-1 1 A7 7 0 0 1 3 4.5 a1 1 0 0 1 1-1z"/></svg>
        0491325067
        <svg class="icon contact__gap" viewBox="0 0 14 14" fill="none" stroke="#fff" stroke-width="1.2"><rect x="0.6" y="0.6" width="12.8" height="12.8"/><path d="M4 3.5 l2 0 l0.8 2 l-1.2 0.9 a5 5 0 0 0 2.2 2.2 l0.9-1.2 l2 0.8 l0 2 a1 1 0 0 1-1 1 A7 7 0 0 1 3 4.5 a1 1 0 0 1 1-1z"/></svg>
        (03) 95147286
      </p>
      <p class="contact__line">
        <svg class="icon" viewBox="0 0 14 14" fill="none" stroke="#fff" stroke-width="1.2"><rect x="0.6" y="0.6" width="12.8" height="12.8"/><rect x="3" y="4.2" width="8" height="5.6"/><path d="M3 4.2 l4 3 l4-3"/></svg>
        mark@corvanimports.com.au
      </p>
    </div>
  </section>

</body>
</html>
```